Looking for Desginers for an abstract art canvas & poster shopify shop

I want to get a design done for an abstract canvas art & print shop. If possible im looking to create the design based on the lumen or minimal template (im open to suggestions). Mostly I need the creative assets such as banners, images, copywriting, typography etc since im having a hard time to give it a descent look myself.

Target Market(s)

Home decor lovers, abstract art enthusiasts and canvas art enthusiast

Industry/Entity Type

Art

Coding

Coded - Design and coding required

Number of Pages Required

1 page

Colors

Designer to choose only greyscale colors for use in the design.

Requirements
Must have
• Creatives Assets such as banners, images, copy, collection image templates. Please use the velorin logo provided below in at least one of the proposals.
Should not have
• anything that has to be coded into html or css.

```html
<!DOCTYPE html>
<html lang="en">
<head>
<meta charset="utf-8">
<title>Velorin — Abstract Canvas Art</title>
<link rel="stylesheet" href="https://fonts.googleapis.com/css2?family=Roboto:wght@300;400;500;700&family=Montserrat:wght@600&display=swap">
<style>
:root{
  --ink:#111111;
  --night:#0d0d0d;
  --black:#000000;
  --white:#ffffff;
  --accent:#2b2b2b;
  --accent-soft:#6e6e6e;
  --muted:#7a7a7a;
  --body:#8a8a8a;
}
*{box-sizing:border-box;margin:0;padding:0}
html,body{width:1200px;height:2650px;overflow:hidden}
body{position:relative;background:var(--white);font-family:'Roboto',Arial,sans-serif;color:var(--ink)}
.abs{position:absolute}

.promo-bar{left:0;top:0;width:1200px;height:40px;background:var(--night);color:var(--white)}
.promo-text{left:89px;top:10px;font-size:16px;font-weight:500}
.cart-link{left:680px;top:10px;font-size:16px;font-weight:500;display:flex;align-items:center;gap:8px}
.search-box{left:778px;top:2px;width:332px;height:35px;background:var(--white);display:flex;align-items:center;padding-left:10px;gap:10px;color:#777;font-size:16px}

.brand{left:91px;top:62px;font-size:46px;font-weight:300;color:var(--ink);letter-spacing:-0.5px}
.main-nav{left:592px;top:84px;display:flex;gap:48px;font-size:16px;font-weight:500;letter-spacing:.2px}
.main-nav .active{color:var(--accent-soft)}

.hero{left:89px;top:144px;width:1021px;height:461px;
  background:linear-gradient(100deg,#3a2a28 0%,#e3443a 22%,#c23a3c 40%,#d9375a 52%,#1f6fa8 66%,#0f4f86 82%,#1a7ab0 100%);
  display:flex;align-items:center;justify-content:center}
.hero-title{font-family:'Montserrat',Arial,sans-serif;font-weight:600;font-size:92px;color:var(--white);letter-spacing:-1px;margin-top:-10px}
.slider-nav{left:546px;top:624px;display:flex;align-items:center;gap:20px}
.dot{width:11px;height:11px;border-radius:50%;background:var(--ink)}
.dot.current{background:#9a9a9a}

.section-title{font-size:40px;font-weight:700;letter-spacing:.5px;color:var(--ink);line-height:48px}
.arts-title{left:89px;top:696px}
.art-grid{left:89px;top:766px;width:1021px;display:grid;grid-template-columns:repeat(4,248px);grid-auto-rows:312px;column-gap:10px;row-gap:28px}
.art-tile{width:248px;height:259px}
.art-card p{font-size:15.5px;line-height:19px;margin-top:10px;letter-spacing:.2px}
.art-card .price{margin-top:5px;font-weight:500}

.news-title{left:89px;top:1474px}
.news-item{width:402px}
.news-item h3{font-size:24px;font-weight:400;color:var(--accent-soft);letter-spacing:.3px;line-height:30px}
.news-item time{display:block;margin-top:6px;font-size:13.5px;color:var(--muted)}
.news-item p{margin-top:12px;font-size:13.5px;line-height:19px;color:var(--body);text-align:justify}
.news-left{left:89px;top:1528px}
.news-right{left:708px;top:1528px}

.feature-art{left:91px;top:1733px;width:459px;height:478px;
  background:linear-gradient(135deg,#9fd8d2 0%,#6fd6c8 30%,#e2a54a 55%,#d45a2e 70%,#3b7fc6 100%)}
.feature-name{left:588px;top:1848px;font-size:42px;font-weight:700;letter-spacing:.5px}
.feature-price{left:588px;top:1900px;font-size:18px}
.btn{width:209px;height:40px;background:var(--accent);color:var(--white);font-size:16px;font-weight:500;display:flex;align-items:center;justify-content:center;letter-spacing:.3px}
.btn-cart{left:589px;top:2001px}
.btn-buy{left:589px;top:2048px}

.site-footer{left:0;top:2279px;width:1200px;height:371px;background:var(--black);color:var(--white)}
.footer-col{top:66px}
.footer-col h4{font-size:22px;font-weight:500;margin-bottom:26px}
.footer-col p{font-size:16px;line-height:27px}
.col-contact{left:89px}
.col-address{left:405px}
.col-follow{left:647px}
.col-news{left:851px;width:259px}
.socials{display:flex;gap:22px;margin-top:4px}
.social{width:14px;height:14px;border-radius:50%;background:var(--white)}
.email-field{margin-top:-4px;width:259px;height:40px;background:var(--white);color:#888;font-size:15px;padding-left:15px;display:flex;align-items:center;border:1px solid #ccc}
.subscribe{margin-top:4px;width:259px;height:40px;background:#3a3a3a;display:flex;align-items:center;justify-content:center;font-size:15px}
.copyright{left:0;top:331px;width:1200px;text-align:center;font-size:13px}
</style>
</head>
<body>

<div class="abs promo-bar">
  <span class="abs promo-text">Free shipping on orders over $50</span>
  <span class="abs cart-link">
    <svg width="22" height="16" viewBox="0 0 22 16" fill="none" stroke="#fff" stroke-width="1.6"><path d="M1 2h4l3 8h10l2-6H7"/><circle cx="9" cy="14" r="1.3" fill="#fff"/><circle cx="17" cy="14" r="1.3" fill="#fff"/></svg>
    Cart
  </span>
  <div class="abs search-box">
    <svg width="15" height="15" viewBox="0 0 15 15" fill="none" stroke="#333" stroke-width="2"><circle cx="6" cy="6" r="4.5"/><path d="M9.5 9.5l4 4"/></svg>
    Search
  </div>
</div>

<div class="abs brand">Velorin</div>
<nav class="abs main-nav">
  <span class="active">HOME</span><span>PRODUCTS</span><span>PRINTS</span><span>BLOG</span><span>CONTACT US</span>
</nav>

<div class="abs hero" role="img" aria-label="Abstract oil painting with red and blue textured brush strokes">
  <h1 class="hero-title">Velorin</h1>
</div>
<div class="abs slider-nav">
  <svg width="8" height="12" viewBox="0 0 8 12" fill="none" stroke="#111" stroke-width="1.5"><path d="M6 1L1 6l5 5"/></svg>
  <span class="dot"></span><span class="dot current"></span>
  <svg width="8" height="12" viewBox="0 0 8 12" fill="none" stroke="#9a9a9a" stroke-width="1.5"><path d="M2 1l5 5-5 5"/></svg>
</div>

<h2 class="abs section-title arts-title">OUR ARTS</h2>
<div class="abs art-grid">
  <div class="art-card"><div class="art-tile" role="img" aria-label="Purple and green marbled fluid art" style="background:linear-gradient(135deg,#7a16e0,#4bd23a 45%,#8a1cf0 70%,#c04ad8)"></div><p>Lorem ipsum dolor sit amet</p><p class="price">$40.00</p></div>
  <div class="art-card"><div class="art-tile" role="img" aria-label="Grey and white alcohol ink art with gold veins" style="background:linear-gradient(135deg,#e4ecf0,#9aa8b8 45%,#d7e4ec 70%,#c9a25a)"></div><p>Lorem ipsum dolor sit amet</p><p class="price">$40.00</p></div>
  <div class="art-card"><div class="art-tile" role="img" aria-label="Pastel pink painting of a small bird on a branch" style="background:linear-gradient(180deg,#f6e2f5,#eab4e6 50%,#d86aa8 80%,#6f9bc7)"></div><p>Lorem ipsum dolor sit amet</p><p class="price">$40.00</p></div>
  <div class="art-card"><div class="art-tile" role="img" aria-label="Teal and ochre abstract resin art" style="background:linear-gradient(135deg,#1c3b4f,#2a7a8c 35%,#c28b45 60%,#1c5c78)"></div><p>Lorem ipsum dolor sit amet</p><p class="price">$40.00</p></div>
  <div class="art-card"><div class="art-tile" role="img" aria-label="Colourful swirling paint clouds" style="background:linear-gradient(135deg,#e86a6a,#2bb4c8 35%,#f2a560 60%,#d24e8a)"></div><p>Lorem ipsum dolor sit amet</p><p class="price">$40.00</p></div>
  <div class="art-card"><div class="art-tile" role="img" aria-label="Pink and red bold brush stroke painting" style="background:linear-gradient(135deg,#f48a6a,#e0245a 40%,#f59ac4 65%,#6fd8d6)"></div><p>Lorem ipsum dolor sit amet</p><p class="price">$40.00</p></div>
  <div class="art-card"><div class="art-tile" role="img" aria-label="Impressionist sunset over the sea" style="background:linear-gradient(180deg,#8a8fa8,#f0b24a 40%,#f4d04a 60%,#4aa0b8)"></div><p>Lorem ipsum dolor sit amet</p><p class="price">$40.00</p></div>
  <div class="art-card"><div class="art-tile" role="img" aria-label="Blue purple and orange textured palette knife painting" style="background:linear-gradient(160deg,#2a4ac8,#8a4aa8 45%,#f28a2a 75%,#f4a030)"></div><p>Lorem ipsum dolor sit amet</p><p class="price">$40.00</p></div>
</div>

<h2 class="abs section-title news-title">NEWS</h2>
<article class="abs news-item news-left">
  <h3>Lorem ipsum dolor sit amet</h3>
  <time>May 18, 2021</time>
  <p>Lorem ipsum dolor sit amet, consectetur adipiscing elit, sed do eiusmod tempor incididunt ut labore et dolore magna aliqua. Ut enim ad minim veniam, quis nostrud exercitation ullamco laboris nisi ut aliquip ex ea commodo consequat.</p>
</article>
<article class="abs news-item news-right">
  <h3>Lorem ipsum dolor sit amet</h3>
  <time>May 18, 2021</time>
  <p>Lorem ipsum dolor sit amet, consectetur adipiscing elit, sed do eiusmod tempor incididunt ut labore et dolore magna aliqua. Ut enim ad minim veniam, quis nostrud exercitation ullamco laboris nisi ut aliquip ex ea commodo consequat.</p>
</article>

<div class="abs feature-art" role="img" aria-label="Abstract canvas painting with turquoise, orange and red brush strokes"></div>
<h2 class="abs feature-name">ABSTRACT CANVAS ART</h2>
<p class="abs feature-price">$23.00</p>
<div class="abs btn btn-cart">ADD TO CART</div>
<div class="abs btn btn-buy">BUY IT NOW</div>

<footer class="abs site-footer">
  <div class="abs footer-col col-contact">
    <h4>Contact Us</h4>
    <p>Phone : 555-0142-7788</p>
    <p>Email : hello@velorin-studio.com</p>
  </div>
  <div class="abs footer-col col-address">
    <h4>Address</h4>
    <p>48 Harlow Lane</p>
    <p>Brookfield CA</p>
    <p>90210</p>
  </div>
  <div class="abs footer-col col-follow">
    <h4>Follow Us</h4>
    <div class="socials">
      <span class="social" aria-label="Social link one"></span>
      <span class="social" aria-label="Social link two"></span>
      <span class="social" aria-label="Social link three"></span>
    </div>
  </div>
  <div class="abs footer-col col-news">
    <h4>Newsletter</h4>
    <div class="email-field">Email Address</div>
    <div class="subscribe">Subscribe Now</div>
  </div>
  <p class="abs copyright">Copyrights © 2021, Velorin Studio. All rights reserved.</p>
</footer>

</body>
</html>
```